Business Cards / Stationary
Harlow Defense Firm
Project: Business Cards / Stationary
Business Cards / Stationary - Law
Creative Brief
Professional
Gareth P. Harlow
Attorney and Counselor
248 N. Kestrel Court Suite 305 Denton, Texas 76209
gareth@garethharlowlaw.example
www.garethharlowlaw.example
I dont have to have front and back but would like to see concept with Blue logo on back side of card

```html
<!DOCTYPE html>
<html lang="en">
<head>
<meta charset="utf-8">
<title>Harlow Defense Firm — Business Card</title>
<link href="https://fonts.googleapis.com/css2?family=Cinzel:wght@400;600&display=swap" rel="stylesheet">
<style>
  :root {
    --navy: #262f7e;
    --navy-deep: #1f2770;
    --gold: #f0c419;
    --white: #ffffff;
    --frame: #2b3590;
    --ink: #2a3382;
  }
  * { margin: 0; padding: 0; box-sizing: border-box; }
  html, body { width: 1200px; height: 977px; overflow: hidden; background: var(--white); }
  .board {
    position: relative;
    width: 1200px; height: 977px;
    border: 2px solid var(--frame);
    font-family: "Cinzel", "Times New Roman", serif;
  }
  .card { position: absolute; left: 246px; width: 756px; }
  .card-front { top: 61px; height: 395px; box-shadow: 0 2px 6px rgba(0,0,0,.12); }
  .front-upper { position: absolute; inset: 0 0 auto 0; height: 232px; background: var(--white); border: 1px solid #e2e2e2; }
  .sheen { position: absolute; top: 232px; left: 0; right: 0; height: 13px;
    background: linear-gradient(180deg, #f4f4f4 0%, #b9b9bc 55%, #8e8f94 100%); }
  .front-lower { position: absolute; top: 245px; left: 0; right: 0; bottom: 0; background: var(--navy); overflow: hidden; }

  .mark { position: absolute; display: flex; align-items: center; }
  .mark-circle { border-radius: 50%; flex: none; }
  .mark-rule { width: 2px; align-self: stretch; margin: 0 10px 0 12px; }
  .mark-name { line-height: 1; font-weight: 400; letter-spacing: .5px; }

  .card-front .mark { left: 22px; top: 40px; height: 92px; }
  .card-front .mark-circle { width: 90px; height: 90px; border: 6px solid var(--gold); }
  .card-front .mark-rule { background: var(--navy); }
  .card-front .mark-name { color: var(--navy); font-size: 34px; width: 300px; }

  .holder { position: absolute; left: 0; right: 0; top: 148px; text-align: center; color: var(--ink); padding-left: 0; }
  .holder-name { font-size: 36px; font-weight: 400; letter-spacing: 1px; }
  .holder-title { font-size: 19px; font-weight: 600; letter-spacing: 1px; margin-top: 2px; }

  .ghost-ring { position: absolute; left: 120px; top: 8px; width: 180px; height: 130px;
    border: 10px solid rgba(255,255,255,.09); border-radius: 50%; transform: rotate(-12deg); }

  .contact { position: absolute; right: 34px; top: 30px; color: var(--white); font-size: 16px; line-height: 25px; letter-spacing: .6px; text-align: right; list-style: none; }
  .contact .label { margin-right: 10px; }

  .card-back { top: 517px; height: 392px; background: var(--navy-deep); }
  .card-back .mark { left: 104px; top: 140px; height: 96px; }
  .card-back .mark-circle { width: 96px; height: 96px; border: 5px solid var(--white); }
  .card-back .mark-rule { background: var(--white); margin: 0 12px 0 14px; }
  .card-back .mark-name { color: var(--white); font-size: 38px; width: 360px; }
</style>
</head>
<body>
<main class="board">
  <section class="card card-front" aria-label="Card front">
    <div class="front-upper">
      <div class="mark">
        <span class="mark-circle"></span>
        <span class="mark-rule"></span>
        <span class="mark-name">Harlow Defense Firm</span>
      </div>
      <div class="holder">
        <div class="holder-name">Gareth P. Harlow</div>
        <div class="holder-title">Attorney and Counselor</div>
      </div>
    </div>
    <div class="sheen"></div>
    <div class="front-lower">
      <span class="ghost-ring"></span>
      <ul class="contact">
        <li>248 N. Kestrel Court Suite 305</li>
        <li>Denton, Texas 76209</li>
        <li><span class="label">PH:</span>940-555-0142 FAX: 940-555-0187</li>
        <li><span class="label">SITE</span>www.garethharlowlaw.example</li>
        <li><span class="label">MAIL</span>gareth@garethharlowlaw.example</li>
      </ul>
    </div>
  </section>

  <section class="card card-back" aria-label="Card back">
    <div class="mark">
      <span class="mark-circle"></span>
      <span class="mark-rule"></span>
      <span class="mark-name">Harlow Defense Firm</span>
    </div>
  </section>
</main>
</body>
</html>
```